Create Website for new Home services company

We need a website built for a new home services company we are primarily a surface refinishing company that repairs cracks in tubs and resurfaces tubs, sinks or vanities also repainting cabinets as well.

```html
<!DOCTYPE html>
<html lang="en">
<head>
<meta charset="UTF-8">
<title>Brightline Refinishing – Surface Refinishing</title>
<link href="https://fonts.googleapis.com/css2?family=Montserrat:wght@500;600;700;800&family=Open+Sans:wght@400;600;700&display=swap" rel="stylesheet">
<style>
:root{
  --navy:#1d3461;
  --navy-dark:#162a52;
  --orange:#f26b1d;
  --ink:#1f2433;
  --muted:#6b7285;
  --light:#f2f4f8;
  --line:#e2e5ec;
  --white:#ffffff;
}
*{box-sizing:border-box;margin:0;padding:0}
html,body{width:1200px;height:3420px;overflow:hidden}
body{font-family:"Open Sans",Arial,sans-serif;color:var(--ink);background:var(--white);font-size:13px;line-height:1.6}
h1,h2,h3,h4,.btn,.nav a{font-family:"Montserrat",Arial,sans-serif}
.wrap{width:800px;margin:0 auto;position:relative}
.btn{display:inline-block;background:var(--orange);color:var(--white);font-weight:700;font-size:12px;letter-spacing:.5px;padding:11px 22px;border-radius:3px;text-transform:uppercase}

/* wordmark */
.brand{display:flex;align-items:center;gap:10px;font-family:"Open Sans",Arial,sans-serif;font-weight:700;font-size:20px;color:var(--navy);white-space:nowrap}
.brand-dot{width:14px;height:14px;border-radius:50%;background:var(--navy);flex:none}

/* header */
.site-header{height:96px;display:flex;align-items:center}
.site-header .wrap{display:flex;align-items:center;justify-content:space-between}
.header-right{display:flex;align-items:center;gap:18px;font-size:13px}
.header-right b{font-family:"Montserrat",sans-serif;color:var(--navy)}
.socials{display:flex;gap:8px}
.socials span{width:18px;height:18px;border-radius:50%;background:var(--navy);display:block}

/* hero */
.hero{height:524px;position:relative;background:linear-gradient(180deg,#3a3f4b 0%,#6d6356 45%,#8a7a66 70%,#4a4640 100%);color:var(--white);text-align:center}
.hero::after{content:"";position:absolute;inset:0;background:rgba(20,32,60,.45)}
.nav{position:absolute;top:0;left:0;right:0;height:38px;background:rgba(22,42,82,.92);z-index:2}
.nav .wrap{display:flex;gap:40px;height:38px;align-items:center}
.nav a{color:var(--white);font-size:11px;font-weight:600;text-decoration:none;letter-spacing:.5px}
.hero-body{position:relative;z-index:2;padding-top:112px}
.hero h1{font-size:44px;line-height:1.12;font-weight:800;text-transform:uppercase;letter-spacing:.5px}
.hero p{margin-top:18px;font-size:14px;opacity:.9}
.hero .btn{margin-top:26px;font-size:15px;padding:14px 30px}
.hero small{display:block;margin-top:16px;font-size:12px;opacity:.85}

/* features */
.features{height:220px;display:flex;align-items:center;border-bottom:1px solid var(--line)}
.features .wrap{display:flex;justify-content:space-between;padding:0 40px}
.feature{width:200px;text-align:center}
.feature svg{width:52px;height:52px}
.feature h3{font-size:14px;font-weight:700;margin-top:10px;color:var(--ink)}
.feature p{font-size:11px;color:var(--muted);margin-top:4px}

/* welcome */
.welcome{height:440px;display:flex;align-items:center}
.welcome .wrap{display:flex;gap:32px;align-items:center}
.welcome-photo{width:380px;height:340px;background:linear-gradient(135deg,#c9c2b6,#8c96a6 60%,#5d6a80);position:relative;flex:none}
.photo-tag{position:absolute;left:0;bottom:28px;background:var(--navy);color:var(--white);font-size:11px;font-weight:600;padding:8px 16px}
.play{position:absolute;left:50%;top:50%;width:54px;height:54px;margin:-27px;border-radius:50%;background:var(--white);display:flex;align-items:center;justify-content:center}
.eyebrow{color:var(--orange);font-family:"Montserrat",sans-serif;font-size:12px;font-weight:700;letter-spacing:3px}
.welcome h2{font-size:30px;line-height:1.2;color:var(--navy);font-weight:800;margin:6px 0 14px}
.welcome p{font-size:12px;color:var(--muted);margin-bottom:12px}
.welcome .btn{margin-top:6px}

/* services */
.services{height:510px;background:var(--light);padding-top:36px;text-align:center}
.section-title{font-size:26px;font-weight:800;color:var(--navy);text-transform:uppercase}
.section-sub{font-size:11px;color:var(--muted);margin-top:2px}
.cards{display:flex;gap:22px;justify-content:center;margin-top:22px}
.card{width:252px;background:var(--white);text-align:left;box-shadow:0 2px 8px rgba(0,0,0,.06)}
.card-photo{height:150px}
.card-body{padding:14px 16px 16px;text-align:center}
.card h3{font-size:17px;font-weight:600;color:var(--ink)}
.card p{font-size:11px;color:var(--muted);margin:6px 0 8px;line-height:1.5}
.learn{display:inline-flex;align-items:center;gap:6px;color:var(--orange);font-size:11px;font-weight:700}
.learn i{width:12px;height:12px;background:var(--orange);display:inline-block}
.rating{margin-top:24px;font-size:13px;color:var(--ink)}
.rating .stars{color:var(--orange);letter-spacing:2px;font-size:15px}
.services .btn{margin-top:14px}

/* estimate */
.estimate{height:390px;background:var(--navy);color:var(--white);display:flex;align-items:center}
.estimate .wrap{display:flex;justify-content:space-between;align-items:center}
.estimate-copy{width:340px}
.estimate h2{font-size:30px;font-weight:800}
.estimate p{font-size:12px;opacity:.85;margin-top:10px}
.form{width:400px;background:var(--white);padding:24px;color:var(--ink)}
.form-row{display:flex;gap:14px}
.field{flex:1;margin-bottom:14px}
.field label{display:block;font-size:11px;color:var(--muted);margin-bottom:4px}
.field div{height:30px;border:1px solid var(--line);background:#fafbfc}
.field .area{height:90px}
.form small{display:block;font-size:9px;color:var(--muted);margin-bottom:12px}

/* premium */
.premium{height:480px;display:flex}
.premium-photo{width:560px;height:480px;background:linear-gradient(160deg,#dcdcd8,#a9aba8 45%,#7d7f7c 75%,#5e5f5b);flex:none}
.premium-copy{padding:64px 0 0 40px;width:440px}
.premium h2{font-size:28px;line-height:1.2;color:var(--navy);font-weight:800}
.premium p{font-size:12px;color:var(--muted);margin:12px 0 18px}
.lists{display:flex;gap:40px}
.lists h4{font-size:12px;font-weight:800;color:var(--navy);margin-bottom:6px}
.lists ul{list-style:none}
.lists li{font-size:11px;display:flex;align-items:center;gap:8px;line-height:2}
.lists li svg{width:12px;height:12px;flex:none}
.premium .btn{margin-top:20px}

/* blog */
.blog{height:450px;padding-top:56px;text-align:center}
.posts{display:flex;gap:22px;justify-content:center;margin-top:24px;text-align:left}
.post{width:252px}
.post-photo{height:170px}
.meta{font-size:10px;color:var(--muted);margin-top:10px}
.post h3{font-size:14px;font-weight:700;line-height:1.3;margin-top:4px;color:var(--ink)}
.post p{font-size:11px;color:var(--muted);margin-top:6px;line-height:1.5}
.read{color:var(--orange);font-size:11px;font-weight:700;margin-top:6px;display:block}

/* newsletter */
.newsletter{height:80px;background:var(--navy-dark);color:var(--white);display:flex;align-items:center}
.newsletter .wrap{display:flex;justify-content:space-between;align-items:center}
.newsletter h3{font-size:17px;font-weight:700}
.subscribe{display:flex}
.subscribe div{width:210px;height:34px;background:var(--white);font-size:11px;color:var(--muted);padding:8px 12px}
.subscribe .btn{border-radius:0;padding:10px 18px}

/* footer */
.site-footer{height:230px;background:var(--navy);color:var(--white);border-top:1px solid rgba(255,255,255,.15)}
.footer-cols{display:flex;gap:36px;padding-top:34px}
.footer-cols h4{font-size:12px;font-weight:800;margin-bottom:8px;letter-spacing:.5px}
.footer-about{width:210px}
.footer-about .brand{color:var(--white);font-size:17px}
.footer-about .brand-dot{background:var(--white)}
.footer-about p{font-size:10px;opacity:.8;margin-top:10px;line-height:1.5}
.footer-cols ul{list-style:none;font-size:10px;line-height:2;opacity:.85}
.contact li{display:flex;gap:6px;align-items:center;white-space:nowrap}
.contact svg{width:11px;height:11px;flex:none}
.estimates .phone{font-family:"Montserrat",sans-serif;color:var(--orange);font-weight:800;font-size:20px}
.estimates .socials{margin-top:6px}
.estimates .socials span{background:var(--white)}
.copyright{text-align:center;font-size:10px;opacity:.7;margin-top:30px}
</style>
</head>
<body>

<header class="site-header">
  <div class="wrap">
    <div class="brand"><span class="brand-dot"></span>Brightline Refinishing</div>
    <div class="header-right">
      <span>Call Today: <b>123 456 7890</b></span>
      <div class="socials"><span></span><span></span><span></span></div>
      <a class="btn">Request a Quote</a>
    </div>
  </div>
</header>

<section class="hero" role="img" aria-label="Kitchen with freshly refinished wooden cabinets and countertop">
  <nav class="nav"><div class="wrap">
    <a>HOME</a><a>SERVICES</a><a>PORTFOLIO</a><a>ABOUT US</a><a>BLOG</a><a>CONTACT US</a>
  </div></nav>
  <div class="hero-body">
    <h1>Keep Your Home<br>Comfortable With Our<br>Refinishing Services</h1>
    <p>Our surface refinishing services can help you bring your floors back to life</p>
    <a class="btn">Call Now 123 456 7890</a>
    <small>Full Service - The Best Completion Is a Service</small>
  </div>
</section>

<section class="features">
  <div class="wrap">
    <div class="feature">
      <svg viewBox="0 0 52 52" fill="none" stroke="#f26b1d" stroke-width="2"><path d="M26 6l16 6v12c0 11-7 19-16 22C17 43 10 35 10 24V12z"/><path d="M19 26l5 5 9-10"/></svg>
      <h3>Trusted Surface Professionals</h3>
      <p>Lorem ipsum dolor sit amet consecte</p>
    </div>
    <div class="feature">
      <svg viewBox="0 0 52 52" fill="none" stroke="#f26b1d" stroke-width="2"><circle cx="26" cy="24" r="15"/><path d="M18 36l-4 10 7-3 5 5M34 36l4 10-7-3-5 5"/><path d="M20 24l4 4 8-8"/></svg>
      <h3>100% Satisfaction Guarantee</h3>
      <p>Lorem ipsum dolor sit amet consecte</p>
    </div>
    <div class="feature">
      <svg viewBox="0 0 52 52" fill="none" stroke="#f26b1d" stroke-width="2"><rect x="9" y="12" width="34" height="30" rx="2"/><path d="M9 20h34M17 8v8M35 8v8M20 31l4 4 8-8"/></svg>
      <h3>Instant Online Booking</h3>
      <p>Lorem ipsum dolor sit amet consecte</p>
    </div>
  </div>
</section>

<section class="welcome">
  <div class="wrap">
    <div class="welcome-photo" role="img" aria-label="Homeowner relaxing beside a newly resurfaced kitchen counter">
      <span class="play"><svg width="16" height="18" viewBox="0 0 16 18"><path d="M2 1l13 8-13 8z" fill="#f26b1d"/></svg></span>
      <span class="photo-tag">Quality Services</span>
    </div>
    <div class="welcome-copy">
      <div class="eyebrow">WHO WE ARE</div>
      <h2>Welcome to Brightline<br>Refinishing</h2>
      <p>Our surface refinishing services can help you bring your floors back to life with expert care and lasting results. Quis aute irure dolor in reprehenderit in voluptate velit esse cillum dolore eu fugiat nulla pariatur.</p>
      <p>Aliquam in lacus semper aliquam egestas mauris vel nunc. Ut enim ad minim veniam quis nostrud exercitation ullamco laboris nisi ut aliquip ex ea commodo consequat duis aute irure.</p>
      <a class="btn">Learn More</a>
    </div>
  </div>
</section>

<section class="services">
  <h2 class="section-title">Our Services</h2>
  <p class="section-sub">Select one of our services and book now</p>
  <div class="cards">
    <div class="card">
      <div class="card-photo" role="img" aria-label="Resurfaced bathroom sink" style="background:linear-gradient(135deg,#e9e6df,#b9b3a6)"></div>
      <div class="card-body"><h3>Surface Refinishing</h3><p>Lorem ipsum dolor sit amet consectetur adipiscing elit sed do eiusmod tempor.</p><span class="learn">Learn More <i></i></span></div>
    </div>
    <div class="card">
      <div class="card-photo" role="img" aria-label="Freshly resurfaced white bathtub" style="background:linear-gradient(135deg,#f2f2f0,#c5c8cc)"></div>
      <div class="card-body"><h3>Resurfaces Tubs</h3><p>Lorem ipsum dolor sit amet consectetur adipiscing elit sed do eiusmod tempor.</p><span class="learn">Learn More <i></i></span></div>
    </div>
    <div class="card">
      <div class="card-photo" role="img" aria-label="Repainted wooden cabinet doors" style="background:linear-gradient(135deg,#e8d9c4,#a8825a)"></div>
      <div class="card-body"><h3>Repainting Cabinets</h3><p>Lorem ipsum dolor sit amet consectetur adipiscing elit sed do eiusmod tempor.</p><span class="learn">Learn More <i></i></span></div>
    </div>
  </div>
  <p class="rating"><span class="stars">★★★★★</span> 4.9 out of 10,023 ratings our services</p>
  <a class="btn">More Services</a>
</section>

<section class="estimate">
  <div class="wrap">
    <div class="estimate-copy">
      <h2>Need An Estimate?</h2>
      <p>Fill out this form and we will be in contact with you shortly.</p>
      <p>Our surface refinishing services can help you bring your floors back to life. Lorem ipsum dolor sit amet consectetur adipiscing elit sed do eiusmod tempor incididunt ut labore et dolore magna aliqua.</p>
    </div>
    <div class="form">
      <div class="form-row">
        <div class="field"><label>Your Name</label><div></div></div>
        <div class="field"><label>Email Address</label><div></div></div>
      </div>
      <div class="field"><label>Message</label><div class="area"></div></div>
      <small>This site is protected by reCAPTCHA and the privacy policy applies.</small>
      <a class="btn">Send Message</a>
    </div>
  </div>
</section>

<section class="premium">
  <div class="premium-photo" role="img" aria-label="Refinished shower floor with drain and glass door"></div>
  <div class="premium-copy">
    <h2>Premium Resurfacing/<br>Refinishing</h2>
    <p>Our surface refinishing services can help you bring your floors back to life. Lorem ipsum dolor sit amet consectetur adipiscing elit sed do eiusmod tempor incididunt.</p>
    <div class="lists">
      <div>
        <h4>RESURFACING</h4>
        <ul>
          <li><svg viewBox="0 0 12 12"><rect width="12" height="12" rx="2" fill="#f26b1d"/><path d="M3 6l2 2 4-4" stroke="#fff" stroke-width="1.5" fill="none"/></svg>Bathtub Resurfacing</li>
          <li><svg viewBox="0 0 12 12"><rect width="12" height="12" rx="2" fill="#f26b1d"/><path d="M3 6l2 2 4-4" stroke="#fff" stroke-width="1.5" fill="none"/></svg>Shower Resurfacing</li>
          <li><svg viewBox="0 0 12 12"><rect width="12" height="12" rx="2" fill="#f26b1d"/><path d="M3 6l2 2 4-4" stroke="#fff" stroke-width="1.5" fill="none"/></svg>Sink Resurfacing</li>
          <li><svg viewBox="0 0 12 12"><rect width="12" height="12" rx="2" fill="#f26b1d"/><path d="M3 6l2 2 4-4" stroke="#fff" stroke-width="1.5" fill="none"/></svg>Tile Resurfacing</li>
          <li><svg viewBox="0 0 12 12"><rect width="12" height="12" rx="2" fill="#f26b1d"/><path d="M3 6l2 2 4-4" stroke="#fff" stroke-width="1.5" fill="none"/></svg>Shower Resurfacing</li>
        </ul>
      </div>
      <div>
        <h4>REFINISHING</h4>
        <ul>
          <li><svg viewBox="0 0 12 12"><rect width="12" height="12" rx="2" fill="#f26b1d"/><path d="M3 6l2 2 4-4" stroke="#fff" stroke-width="1.5" fill="none"/></svg>Bathtub Refinishing</li>
          <li><svg viewBox="0 0 12 12"><rect width="12" height="12" rx="2" fill="#f26b1d"/><path d="M3 6l2 2 4-4" stroke="#fff" stroke-width="1.5" fill="none"/></svg>Shower Refinishing</li>
          <li><svg viewBox="0 0 12 12"><rect width="12" height="12" rx="2" fill="#f26b1d"/><path d="M3 6l2 2 4-4" stroke="#fff" stroke-width="1.5" fill="none"/></svg>Sink Refinishing</li>
          <li><svg viewBox="0 0 12 12"><rect width="12" height="12" rx="2" fill="#f26b1d"/><path d="M3 6l2 2 4-4" stroke="#fff" stroke-width="1.5" fill="none"/></svg>Tile Refinishing</li>
          <li><svg viewBox="0 0 12 12"><rect width="12" height="12" rx="2" fill="#f26b1d"/><path d="M3 6l2 2 4-4" stroke="#fff" stroke-width="1.5" fill="none"/></svg>Shower Refinishing</li>
        </ul>
      </div>
    </div>
    <a class="btn">View Details</a>
  </div>
</section>

<section class="blog">
  <h2 class="section-title">Latest From Blog</h2>
  <div class="posts">
    <article class="post">
      <div class="post-photo" role="img" aria-label="Bathroom vanity sink being refinished" style="background:linear-gradient(135deg,#ebe7e0,#a9a196)"></div>
      <div class="meta">June 12, 2023 &nbsp;|&nbsp; 2 Comments</div>
      <h3>The Process of Surface Refinishing Step-by-Step Guide</h3>
      <p>Lorem ipsum dolor sit amet consectetur adipiscing elit sed do eiusmod tempor.</p>
      <span class="read">Read More</span>
    </article>
    <article class="post">
      <div class="post-photo" role="img" aria-label="Close view of a refinished stone countertop" style="background:linear-gradient(135deg,#d8c7ad,#8f7456)"></div>
      <div class="meta">June 12, 2023 &nbsp;|&nbsp; 2 Comments</div>
      <h3>The Latest Trends in Surface Refinishing Colors and Finishes</h3>
      <p>Lorem ipsum dolor sit amet consectetur adipiscing elit sed do eiusmod tempor.</p>
      <span class="read">Read More</span>
    </article>
    <article class="post">
      <div class="post-photo" role="img" aria-label="Bright bathroom with refinished tub and tiles" style="background:linear-gradient(135deg,#eef0f2,#a7b0ba)"></div>
      <div class="meta">June 12, 2023 &nbsp;|&nbsp; 2 Comments</div>
      <h3>Expert Tips for Maintaining Your Refinished Surfaces</h3>
      <p>Lorem ipsum dolor sit amet consectetur adipiscing elit sed do eiusmod tempor.</p>
      <span class="read">Read More</span>
    </article>
  </div>
</section>

<section class="newsletter">
  <div class="wrap">
    <h3>Subscribe to our Newsletter</h3>
    <div class="subscribe"><div>Email Address</div><a class="btn">Subscribe</a></div>
  </div>
</section>

<footer class="site-footer">
  <div class="wrap">
    <div class="footer-cols">
      <div class="footer-about">
        <div class="brand"><span class="brand-dot"></span>Brightline Refinishing</div>
        <p>Welcome to Brightline Refinishing. Lorem ipsum dolor sit amet consectetur adipiscing elit sed do eiusmod.</p>
      </div>
      <div>
        <h4>QUICK LINKS</h4>
        <ul><li>Services</li><li>Projects</li><li>Blog</li><li>About Us</li><li>Contact Us</li></ul>
      </div>
      <div class="contact">
        <h4>CONTACT</h4>
        <ul>
          <li><svg viewBox="0 0 12 12"><path d="M6 1a3.5 3.5 0 00-3.5 3.5C2.5 7.5 6 11 6 11s3.5-3.5 3.5-6.5A3.5 3.5 0 006 1z" fill="#f26b1d"/></svg>1458 Maple Ridge Rd, Larkfield, OR</li>
          <li><svg viewBox="0 0 12 12"><rect x="1" y="3" width="10" height="7" fill="none" stroke="#f26b1d"/><path d="M1 3l5 4 5-4" fill="none" stroke="#f26b1d"/></svg>hello@brightlinerefinishing.example</li>
          <li><svg viewBox="0 0 12 12"><path d="M3 1l2 2-1 2c1 1.5 2 2.5 3 3l2-1 2 2-1.5 2C5 10.5 1.5 7 1 2.5z" fill="#f26b1d"/></svg>PHONE 123 456 7890</li>
        </ul>
      </div>
      <div class="estimates">
        <h4>GET FREE ESTIMATES</h4>
        <div class="phone">123 456 7890</div>
        <h4 style="margin-top:14px">FOLLOW US</h4>
        <div class="socials"><span></span><span></span><span></span></div>
      </div>
    </div>
    <p class="copyright">© 2023 Brightline Refinishing. All Rights Reserved</p>
  </div>
</footer>

</body>
</html>
```